Business card for acupunctist in Melbourne. Specialises in Fertility, pre and post natal care, pain

I am looking for a business card which is going to catch people eyes. Two sided, one side in a muted colour (keeping it feminine) (pink or yellow???)maybe with a little simple logo or picture, the other side I was thinking white with 3 colours (pink grey and yellow... Had these in mind.
Info on the card
Marla Quenby Acupuncture

Dr Marla Quenby (TCM Acupuncture)
Acupuncture for balancing body and mind.
Fernleaf Wellcraft
14 Corran Lane, Elsworth 3071.
94726150
0438219574
Marlatcm@quenbymail.com

Some other little logo/ designs I have liked are as follows:
http://www.dorisfelkaclinic.com/rates-and-insurance/
http://www.corinnetavish.com/
http://www.rz-needlework.co.uk/

Target Market(s)

professional women, people in pain, active people, people seeking a healthy lifefstyle.

Industry/Entity Type

Business

Font styles to use
Serif
Sans Serif

Colors
eea4c8
fde08a
aaaaaa

Requirements
Must have
• Must be eye catching, but not too loud and busy. Subltle is good. Simple is also good. The logo could be something that represents growth and health and nurturing. Again not too elaborate, very simple.
Thankyou
Should not have
• Electric colours, crazy fonts, Pictures of yin and yang, candles, or bodies.

```html
<!DOCTYPE html>
<html lang="en">
<head>
<meta charset="utf-8">
<title>Marla Quenby Acupuncture – Business Card</title>
<link href="https://fonts.googleapis.com/css2?family=Ubuntu:wght@400;500;700&family=Tinos&display=swap" rel="stylesheet">
<style>
  :root {
    --page-bg: #ececec;
    --card-white: #ffffff;
    --band-grey: #aaaaaa;
    --rule-light: #f4f4f4;
    --text-on-band: #ffffff;
    --text-dark: #4a4a4a;
    --text-mid: #6f6f6f;
    --text-muted: #9a9a9a;
    --accent-pink: #eea4c8;
    --accent-yellow: #fde08a;
    --front-bg: #fbf3df;
    --front-bg-light: #fdf8ec;
    --band-yellow: #fde08a;
    --band-edge: #aaaaaa;
    --ink: #4a4a4a;
    --photo-light: #f6eed6;
    --photo-mid: #d9dcc4;
    --photo-deep: #b7bea0;
  }
  * { margin: 0; padding: 0; box-sizing: border-box; }
  html, body {
    width: 1200px; height: 900px; overflow: hidden;
    background: var(--page-bg);
    font-family: "Ubuntu", sans-serif;
  }
  .card {
    position: absolute; left: 250px;
    width: 700px; height: 400px; overflow: hidden;
    border-radius: 4px;
    box-shadow: 0 2px 8px rgba(0,0,0,0.12);
  }

  /* ---------- Contact side ---------- */
  .card-contact { top: 40px; background: var(--card-white); color: var(--text-dark); }
  .contact-band {
    position: absolute; left: 0; right: 0; top: 48px; height: 112px;
    background: var(--band-grey);
    border-top: 3px double var(--rule-light);
    border-bottom: 3px double var(--rule-light);
    box-shadow: 0 -1px 0 var(--band-grey), 0 1px 0 var(--band-grey);
  }
  .contact-photo {
    position: absolute; left: 150px; top: 28px; width: 118px; height: 128px;
    background: linear-gradient(135deg, #f7efe8 0%, #ecd3c0 45%, #dcb49a 75%, #f3e8e0 100%);
  }
  .practice-name {
    position: absolute; left: 300px; top: 58px;
    font-size: 26px; font-weight: 500; letter-spacing: -0.3px;
    color: var(--text-on-band);
  }
  .practitioner {
    position: absolute; right: 34px; top: 104px; text-align: right;
    color: var(--text-on-band);
  }
  .practitioner-name { font-size: 25px; font-weight: 400; letter-spacing: 0.5px; line-height: 1.05; }
  .practitioner-role { font-size: 14px; letter-spacing: 0.5px; }
  .clinic-name {
    position: absolute; left: 60px; top: 180px;
    font-size: 30px; font-weight: 500; line-height: 1.1; letter-spacing: -0.5px;
    color: var(--text-dark);
  }
  .clinic-address {
    position: absolute; left: 60px; top: 298px;
    font-size: 12px; color: var(--text-muted);
  }
  .contact-list {
    position: absolute; right: 40px; top: 226px; list-style: none;
  }
  .contact-item {
    display: flex; align-items: center; justify-content: flex-end; gap: 18px;
    font-size: 14px; color: var(--text-mid); margin-bottom: 22px; line-height: 1.15; text-align: right;
  }
  .contact-icon { width: 30px; height: 30px; flex: none; }
  .contact-foot {
    position: absolute; left: 0; right: 0; bottom: 0; height: 34px;
    background: var(--band-grey);
    border-top: 3px double var(--rule-light);
  }

  /* ---------- Brand side ---------- */
  .card-brand {
    top: 470px;
    background: linear-gradient(160deg, var(--front-bg-light) 0%, var(--front-bg) 70%);
  }
  .brand-photo {
    position: absolute; right: 0; top: 0; width: 410px; height: 230px;
    background: radial-gradient(ellipse at 60% 45%, var(--photo-deep) 0%, var(--photo-mid) 40%, var(--photo-light) 70%, rgba(251,243,223,0) 100%);
  }
  .brand-mark {
    position: absolute; left: 140px; top: 170px;
    display: flex; align-items: center; gap: 14px;
  }
  .brand-dot { width: 22px; height: 22px; border-radius: 50%; background: var(--accent-pink); flex: none; }
  .brand-name { font-size: 36px; font-weight: 700; color: var(--ink); letter-spacing: -0.8px; }
  .brand-tagline {
    position: absolute; left: 176px; top: 222px;
    font-family: "Tinos", serif; font-size: 19px; color: var(--ink);
  }
  .brand-band {
    position: absolute; left: 0; right: 0; bottom: 0; height: 126px;
    background: var(--band-yellow);
    border-top: 6px solid var(--band-edge);
  }
</style>
</head>
<body>

<section class="card card-contact">
  <div class="contact-band"></div>
  <div class="contact-photo" role="img" aria-label="Photo of a relaxing therapy treatment"></div>
  <p class="practice-name">Fernleaf Wellcraft</p>
  <div class="practitioner">
    <p class="practitioner-name">Dr Marla Quenby</p>
    <p class="practitioner-role">TCM Acupuncture</p>
  </div>
  <h1 class="clinic-name">Marla<br>Quenby<br>Acupuncture</h1>
  <p class="clinic-address">14 Corran Lane, Elsworth 3071.</p>
  <ul class="contact-list">
    <li class="contact-item">
      <span>94726150<br>0438219574</span>
      <svg class="contact-icon" viewBox="0 0 30 30" aria-hidden="true">
        <path d="M4 11 Q15 3 26 11 L24 14 L19 13 L19 10 Q15 8.5 11 10 L11 13 L6 14 Z" fill="var(--accent-pink)"/>
        <rect x="7" y="15" width="16" height="11" rx="2" fill="var(--accent-pink)"/>
        <circle cx="15" cy="20.5" r="3" fill="var(--card-white)"/>
      </svg>
    </li>
    <li class="contact-item">
      <span>Marlatcm@quenbymail.com</span>
      <svg class="contact-icon" viewBox="0 0 30 30" aria-hidden="true" fill="none" stroke="var(--accent-pink)" stroke-width="2">
        <circle cx="15" cy="15" r="12"/>
        <ellipse cx="15" cy="15" rx="5" ry="12"/>
        <line x1="3" y1="15" x2="27" y2="15"/>
        <line x1="5" y1="9" x2="25" y2="9"/>
        <line x1="5" y1="21" x2="25" y2="21"/>
      </svg>
    </li>
  </ul>
  <div class="contact-foot"></div>
</section>

<section class="card card-brand">
  <div class="brand-photo" role="img" aria-label="Close-up photo of a leaf with a water drop"></div>
  <div class="brand-mark">
    <span class="brand-dot"></span>
    <h2 class="brand-name">Marla Quenby Acupuncture</h2>
  </div>
  <p class="brand-tagline">Acupuncture for balancing body and mind</p>
  <div class="brand-band"></div>
</section>

</body>
</html>
```